Casas de Nueva Aurora Flyer

Make me a flyer postcard 5 x 7 horizontal, one sided. I want main title to be "Casas de Nueva Aurora". It needs to say “Familias que se forman en la fe y valores humanos, y trabajan para llevar a otras familias al encuentro con Cristo y la Virgen María.”  We are in 4 places, include this:
Reuniones Cada Domingo
Los Olmos, Falls Church: 11:15am - 301-555-0142
Monte Claro, Sterling: 9:30am - 571-555-0187
Hogar Valle Sereno, 9:45am - 703-555-0163
Puerta Dorada, Winchester: 2:30pm - 540-555-0129
Include the logo attached, and use the picture attached as the main image, you can select the people from the image only and delete background or keep background but make it fit in nicely to the postcard.

```html
<!DOCTYPE html>
<html lang="es">
<head>
<meta charset="utf-8">
<title>Casas de Nueva Aurora</title>
<link rel="stylesheet" href="https://fonts.googleapis.com/css2?family=Cinzel:wght@500;600;700&family=Red+Hat+Display:wght@500;700;800;900&display=swap">
<style>
  :root {
    --navy: #1a3060;
    --navy-deep: #152a57;
    --sky: #2a7fd0;
    --cream: #f8deb0;
    --red: #e3300f;
    --ink: #1a1a1a;
    --rule: #d8d8d8;
    --backdrop: #bdbdbd;
  }
  * { margin: 0; padding: 0; box-sizing: border-box; }
  html, body { width: 1200px; height: 1117px; overflow: hidden; background: var(--backdrop); }
  .postcard-frame { position: absolute; left: 50px; top: 166px; width: 1100px; height: 785px; }
  .postcard {
    position: absolute; left: 0; top: 0; width: 1730px; height: 1235px;
    transform: scale(0.63584); transform-origin: 0 0;
    background: #fff; overflow: hidden;
    font-family: "Red Hat Display", sans-serif;
  }
  .hero {
    position: absolute; left: 0; top: 0; width: 1730px; height: 922px;
    background: radial-gradient(circle at 230px 320px, #2e86d6 0%, #1f5aa6 22%, var(--navy) 45%, var(--navy-deep) 100%);
  }
  .hero-glow {
    position: absolute; right: 0; top: 572px; width: 700px; height: 350px;
    background: radial-gradient(ellipse at 100% 100%, #2a84dc 0%, rgba(42,132,220,0.4) 40%, rgba(26,48,96,0) 75%);
  }
  .group-photo {
    position: absolute; left: 455px; top: 0; width: 1275px; height: 572px;
    background: linear-gradient(180deg, #e89a8a 0%, #f4b878 30%, #f2c36a 50%, #7f7fa0 78%, #8a6a4f 100%);
  }
  .arc-band { position: absolute; left: 0; top: 0; width: 700px; height: 600px; }
  .icon-frame {
    position: absolute; left: 135px; top: 165px; width: 315px; height: 447px;
    clip-path: polygon(50% 0, 100% 15%, 100% 100%, 0 100%, 0 15%);
    background: linear-gradient(160deg, #b49a52 0%, #d63a22 30%, #c8261a 60%, #e08a2a 85%, #8e7a3e 100%);
    box-shadow: 0 10px 20px rgba(0,0,0,.4);
  }
  .title {
    position: absolute; left: 132px; top: 636px; width: 780px;
    font-family: "Cinzel", serif; font-weight: 600; color: var(--cream);
    font-size: 90px; line-height: 96px; letter-spacing: -1px; white-space: nowrap;
  }
  .title .small { font-size: 54px; }
  .mission {
    position: absolute; left: 938px; top: 645px; width: 690px;
    color: #fff; font-weight: 500; font-size: 30px; line-height: 50.5px;
    text-transform: uppercase;
  }
  .meetings-pill {
    position: absolute; left: 370px; top: 868px; width: 1004px; height: 86px;
    background: var(--red); border: 5px solid #fff; border-radius: 43px;
    box-shadow: 0 4px 8px rgba(0,0,0,.25);
    color: #fff; font-weight: 900; font-size: 32px; letter-spacing: 17px; white-space: nowrap;
    display: flex; align-items: center; justify-content: center; padding-left: 17px;
  }
  .locations { position: absolute; left: 0; top: 985px; width: 1730px; height: 200px; }
  .location { position: absolute; top: 0; width: 340px; }
  .location + .location::before {
    content: ""; position: absolute; left: -55px; top: 0; width: 2px; height: 172px; background: var(--rule);
  }
  .location-name { color: var(--red); font-weight: 800; font-size: 28.5px; line-height: 35px; height: 78px; text-transform: uppercase; white-space: nowrap; }
  .detail { display: flex; align-items: center; height: 55px; font-size: 29px; font-weight: 500; color: var(--ink); }
  .detail svg { width: 36px; height: 36px; margin-right: 38px; flex: none; }
</style>
</head>
<body>
<div class="postcard-frame">
  <div class="postcard">
    <div class="hero">
      <div class="hero-glow"></div>
      <div class="group-photo" role="img" aria-label="Group photo of the families gathered outdoors under a sunset sky"></div>
      <svg class="arc-band" viewBox="0 0 700 600" aria-hidden="true">
        <path d="M468 -10 C 468 80 440 170 370 240" fill="none" stroke="#f8deb0" stroke-width="74"/>
        <path d="M468 -10 C 468 80 440 170 370 240" fill="none" stroke="#e3300f" stroke-width="56"/>
      </svg>
      <div class="icon-frame" role="img" aria-label="Framed religious icon of the Holy Family"></div>
      <h1 class="title">CASAS <span class="small">DE</span><br>NUEVA AURORA</h1>
      <p class="mission">Familias que se forman en la fe y valores humanos, y trabajan para llevar a otras familias al encuentro con Cristo y la Virgen María.</p>
    </div>
    <div class="meetings-pill">REUNIONES CADA DOMINGO</div>
    <div class="locations">
      <div class="location" style="left:135px">
        <h2 class="location-name">Los Olmos,<br>Falls Church</h2>
        <p class="detail"><svg viewBox="0 0 36 36" fill="none" stroke="#e3300f" stroke-width="2"><rect x="4" y="6" width="28" height="27" rx="3"/><path d="M4 13h28M11 3v6M25 3v6M10 19h16M10 25h16"/></svg>11:15AM</p>
        <p class="detail"><svg viewBox="0 0 36 36" fill="none" stroke="#e3300f" stroke-width="2"><path d="M9 4l6 7-3 4c2 5 5 8 10 10l4-3 7 6-4 5C16 32 4 20 5 8z"/></svg>301-555-0142</p>
      </div>
      <div class="location" style="left:505px">
        <h2 class="location-name">Monte Claro,<br>Sterling</h2>
        <p class="detail"><svg viewBox="0 0 36 36" fill="none" stroke="#e3300f" stroke-width="2"><rect x="4" y="6" width="28" height="27" rx="3"/><path d="M4 13h28M11 3v6M25 3v6M10 19h16M10 25h16"/></svg>9:30AM</p>
        <p class="detail"><svg viewBox="0 0 36 36" fill="none" stroke="#e3300f" stroke-width="2"><path d="M9 4l6 7-3 4c2 5 5 8 10 10l4-3 7 6-4 5C16 32 4 20 5 8z"/></svg>571-555-0187</p>
      </div>
      <div class="location" style="left:900px">
        <h2 class="location-name">Hogar<br>Valle Sereno</h2>
        <p class="detail"><svg viewBox="0 0 36 36" fill="none" stroke="#e3300f" stroke-width="2"><rect x="4" y="6" width="28" height="27" rx="3"/><path d="M4 13h28M11 3v6M25 3v6M10 19h16M10 25h16"/></svg>9:45AM</p>
        <p class="detail"><svg viewBox="0 0 36 36" fill="none" stroke="#e3300f" stroke-width="2"><path d="M9 4l6 7-3 4c2 5 5 8 10 10l4-3 7 6-4 5C16 32 4 20 5 8z"/></svg>703-555-0163</p>
      </div>
      <div class="location" style="left:1273px">
        <h2 class="location-name">Puerta Dorada,<br>Winchester</h2>
        <p class="detail"><svg viewBox="0 0 36 36" fill="none" stroke="#e3300f" stroke-width="2"><rect x="4" y="6" width="28" height="27" rx="3"/><path d="M4 13h28M11 3v6M25 3v6M10 19h16M10 25h16"/></svg>2:30PM</p>
        <p class="detail"><svg viewBox="0 0 36 36" fill="none" stroke="#e3300f" stroke-width="2"><path d="M9 4l6 7-3 4c2 5 5 8 10 10l4-3 7 6-4 5C16 32 4 20 5 8z"/></svg>540-555-0129</p>
      </div>
    </div>
  </div>
</div>
</body>
</html>
```